New Print Material Needed for Renovation Company

We are looking to update our current Print Material to reflect the current process we offer to our clients. A lot of the information is also outdated along with many of the photos that are currently being used. We are a renovation company that specializes in residential and commercial renovations and custom builds.This project is MULTIPLE pages. We will pay the chosen designer an extra fee for the designing 3-4 additional pages that are similar to the chosen design. Attached is our current Print Material. We are hoping to update the look of them and some of the messaging. Our current company colors are white, blue and light grey and it will remain that way.

Industry/Entity Type

Construction Company

Font styles to use
Sans Serif

Colors
3176b5
ffffff

Requirements
Must have
• Easy to explain the process
• Easy to read and understand let alone
• Easy to navigate
Nice to have
• As much creativity as possible
Should not have
• no confusing text
• no confusing layout

```html
<!DOCTYPE html>
<html lang="en">
<head>
<meta charset="utf-8">
<title>Our Coverage at a Glance</title>
<link href="https://fonts.googleapis.com/css2?family=Roboto:wght@500;700&display=swap" rel="stylesheet">
<style>
  :root {
    --brand-blue: #1b57a1;
    --paper: #ffffff;
    --badge-grey: #9aa3ad;
    --photo-light: #d9dde2;
    --photo-mid: #8f969e;
  }
  * { margin: 0; padding: 0; box-sizing: border-box; }
  html, body { width: 849px; height: 1200px; overflow: hidden; background: var(--paper); }
  .sheet {
    position: relative; width: 849px; height: 1200px; overflow: hidden;
    background: var(--paper); font-family: "Roboto", Arial, sans-serif;
  }
  .side-strip { position: absolute; left: 793px; top: 0; width: 56px; height: 1200px; background: var(--brand-blue); }
  .coverage-panel { position: absolute; left: 0; top: 98px; width: 793px; height: 974px; background: var(--brand-blue); }
  .page-title {
    position: absolute; left: 66px; top: 30px;
    font-weight: 700; font-size: 51px; letter-spacing: -0.3px; line-height: 1;
    color: var(--brand-blue);
  }
  .column-title {
    position: absolute; top: 106px;
    font-weight: 700; font-size: 33px; line-height: 1; color: var(--paper);
  }
  .column-title.covered { left: 67px; }
  .column-title.excluded { left: 450px; }
  .item {
    position: absolute; width: 330px;
    font-weight: 500; font-size: 20.5px; line-height: 25.7px; color: var(--paper);
  }
  .item::before {
    content: ""; position: absolute; left: -26px; top: 5px;
    border-left: 15px solid var(--paper);
    border-top: 8px solid transparent; border-bottom: 8px solid transparent;
  }
  .covered-list .item { left: 67px; }
  .excluded-list .item { left: 450px; width: 345px; }
  .room-photo { position: absolute; left: 0; top: 0; }
  .partner-badges { position: absolute; left: 0; top: 1110px; width: 793px; height: 50px; }
  .badge { position: absolute; top: 8px; width: 32px; height: 32px; background: var(--badge-grey); }
  .badge.round { border-radius: 50%; }
</style>
</head>
<body>
<div class="sheet">
  <div class="side-strip"></div>
  <h1 class="page-title">OUR COVERAGE AT A GLANCE</h1>
  <div class="coverage-panel"></div>

  <svg class="room-photo" width="849" height="1200" viewBox="0 0 849 1200">
    <defs>
      <linearGradient id="roomTones" x1="0" y1="0" x2="1" y2="1">
        <stop offset="0" stop-color="#eef0f2"/>
        <stop offset="0.5" stop-color="#b9bec4"/>
        <stop offset="1" stop-color="#5d646c"/>
      </linearGradient>
    </defs>
    <polygon points="675,786 841,954 675,1118 509,954" fill="var(--brand-blue)"/>
    <polygon points="675,803 826,954 675,1105 523,954" fill="url(#roomTones)"
             role="img" aria-label="Photo of a bright bedroom with a made bed and window seat"/>
  </svg>

  <h2 class="column-title covered">WHAT'S COVERED</h2>
  <h2 class="column-title excluded">WHAT'S NOT COVERED</h2>

  <div class="covered-list">
    <p class="item" style="top:153px">Constructed in a workmanlike manner and free from defects in material.</p>
    <p class="item" style="top:250px">Fit for habitation.</p>
    <p class="item" style="top:317px">Constructed in accordance with the provincial Building Code.</p>
    <p class="item" style="top:390px">Free of major structural defects.</p>
    <p class="item" style="top:457px">Defects in materials, including windows, doors and caulking, or defects in work that result in water penetration into the building envelope.</p>
    <p class="item" style="top:594px">Defects in work and materials in the electrical, plumbing and heating delivery and distribution systems.</p>
    <p class="item" style="top:712px">Defects in work or materials which result in the detachment, displacement or deterioration of exterior cladding (such as brickwork, aluminum or vinyl siding).</p>
    <p class="item" style="top:895px">Violations of the provincial building code affecting health and safety (including, but not limited to, violations relating to fire safety and the structural adequacy of the home).</p>
  </div>

  <div class="excluded-list">
    <p class="item" style="top:153px">Damage resulting from improper maintenance such as dampness or condensation caused by the homeowners failure to maintain proper ventilation levels or improper operation of a humidifier, hot tub or other moisture-producing device.</p>
    <p class="item" style="top:380px">Alterations, deletions or additions made by the homeowner.<br>Defects in materials, design and work supplied or installed by the homeowner.</p>
    <p class="item" style="top:522px">Damage caused by the homeowner or visitors.</p>
    <p class="item" style="top:592px">Normal Wear and Tear - scuffs, tears, scratches, normal shrinkage of materials.</p>
    <p class="item" style="top:685px">Third party damage - from municipal services, acts of god, vandalism, damage from insects or rodents.</p>
  </div>

  <div class="partner-badges" aria-label="Partner and award badges">
    <span class="badge" style="left:109px"></span>
    <span class="badge round" style="left:205px"></span>
    <span class="badge" style="left:280px"></span>
    <span class="badge" style="left:347px"></span>
    <span class="badge round" style="left:407px"></span>
    <span class="badge" style="left:465px"></span>
    <span class="badge round" style="left:533px"></span>
    <span class="badge" style="left:605px"></span>
  </div>
</div>
</body>
</html>
```